Meadow Hollow Beauty brand redesign of product labels

national rebrand of skincare product labels - same design but 6 sizes. Will be used for facial serums, body oils, bath salts, room sprays, etc. All labels to be same design - just adjusted for the different sizes. See brand document and sample label.

Bottle Specifications are located in the branding file.
Fonts included in product branding document.
Colours included in branding document.

Featuring company name and logo, product name, product feature, ingredients, size, directions, tag line. See attached sample label as example for design.

Black label base - matt.

Target Market(s)

Natural beauty, 20-60

Industry/Entity Type

farming, natural beauty

Font styles to use
Sans Serif

Requirements
Must have
• Modern, clean, homey
Nice to have
• modern clean design - using the branding colours provided
Should not have
• busy, crowded,

```html
<!DOCTYPE html>
<html lang="en">
<head>
<meta charset="UTF-8">
<title>Meadow Hollow Beauty — Verdel Labels</title>
<link href="https://fonts.googleapis.com/css2?family=Jost:wght@300;400;500&display=swap" rel="stylesheet">
<style>
  :root {
    --page: #ececec;
    --label-black: #0b0c0b;
    --leaf-deep: #2f4a1f;
    --leaf-light: #8fb24a;
    --teal: #93c9c3;
    --cream: #ece9dc;
  }
  html, body {
    margin: 0;
    padding: 0;
    width: 1200px;
    height: 1200px;
    overflow: hidden;
    background: var(--page);
    font-family: "Jost", sans-serif;
  }
  .canvas {
    position: relative;
    width: 1200px;
    height: 1200px;
  }
  .label {
    position: absolute;
    top: 375px;
    width: 400px;
    height: 450px;
    background: var(--label-black);
    color: var(--cream);
    text-align: center;
    overflow: hidden;
  }
  .label--front { left: 150px; }
  .label--back { left: 650px; }
  .foliage {
    position: absolute;
    inset: 0;
    background:
      radial-gradient(ellipse 60% 55% at 50% 50%, var(--label-black) 55%, rgba(11,12,11,0) 100%),
      linear-gradient(135deg, var(--leaf-light) 0%, var(--leaf-deep) 30%, var(--label-black) 50%, var(--leaf-deep) 72%, var(--leaf-light) 100%);
    opacity: 0.85;
  }
  .content {
    position: relative;
    height: 100%;
    display: flex;
    flex-direction: column;
    align-items: center;
  }
  .brand {
    display: flex;
    align-items: center;
    gap: 7px;
    font-size: 11px;
    font-weight: 400;
    letter-spacing: 1.5px;
    text-transform: uppercase;
    color: var(--cream);
  }
  .brand__dot {
    width: 18px;
    height: 18px;
    border: 1px solid var(--cream);
    border-radius: 50%;
  }
  .label--front .brand { margin-top: 115px; }
  .label--back .brand { margin-top: 90px; }
  .product-name {
    margin: 14px 0 0;
    font-weight: 300;
    color: var(--teal);
    letter-spacing: 2px;
  }
  .label--front .product-name { font-size: 58px; line-height: 1; }
  .label--back .product-name { font-size: 36px; line-height: 1; margin-top: 12px; }
  .product-type {
    margin-top: 12px;
    font-size: 15px;
    font-weight: 500;
    letter-spacing: 0.5px;
  }
  .product-feature {
    margin-top: 12px;
    font-size: 11.5px;
    letter-spacing: 0.3px;
  }
  .product-size {
    margin-top: 24px;
    font-size: 19px;
    font-weight: 300;
  }
  .info {
    margin-top: 16px;
    width: 150px;
    font-size: 10px;
    line-height: 1.25;
    text-transform: uppercase;
  }
  .info__title {
    font-weight: 500;
    margin: 0 0 2px;
  }
  .info__text { margin: 0 0 10px; font-weight: 400; }
</style>
</head>
<body>
<main class="canvas">
  <section class="label label--front">
    <div class="foliage" role="img" aria-label="Watercolour willow leaf branches framing the label edges"></div>
    <div class="content">
      <div class="brand"><span class="brand__dot"></span>Meadow Hollow Beauty</div>
      <h1 class="product-name">VERDEL</h1>
      <div class="product-type">HAIR TREATMENT OIL</div>
      <div class="product-feature">CONSENTRATED SOOTHING MIST</div>
      <div class="product-size">1.0fl oz/ 30ml</div>
    </div>
  </section>

  <section class="label label--back">
    <div class="foliage" role="img" aria-label="Watercolour willow leaf branches framing the label edges"></div>
    <div class="content">
      <div class="brand"><span class="brand__dot"></span>Meadow Hollow Beauty</div>
      <h2 class="product-name">VERDEL</h2>
      <div class="info">
        <p class="info__title">Ingredients</p>
        <p class="info__text">Nunc dolor tortor, vulputate vitae accumsan non, gravida quis elit.</p>
        <p class="info__title">Directions</p>
        <p class="info__text">Maecenas at egestas magna. Cras malesuada porttitor facilisis. Duis non est erat, amet quis dui.</p>
      </div>
    </div>
  </section>
</main>
</body>
</html>
```